Vora Kest Cleansers Trading L.L.C

We need stationary design for our new company contain ( Business card - head latter - envelops( big & small) - folder file ) One identity and creative design & has related with logo colors ....A unified identity
The main elements of the design that includes the main logos (logo vora + vora logo membership Saif bin Harun) as it is in the attachment then the address of the company.
The Address is
Ras Kulaib - Next to Nuwar Plaza Mall
Fanar Trade Tower - 614
P.O.Box : 48207 Dubai - U.A.E
Tel. : 00971 4 57 86 204
Fax : 00971 4 57 86 205
Email : info@vorakestclean.example
www.vorakestclean.example
Please read the attachment in an important way, especially the terms of the government logo (Saif Bin Harun Membership)
In the design of business cards .. Please put slogans (Pivo Fresh Range - Pivo Professional - Khubrat ) be in the back of the card
Put my name sample
Sami Yousef Hamdan Jaber
Director Manager
Mobil : + 971 55 839 0 839

```html
<!DOCTYPE html>
<html lang="en">
<head>
<meta charset="utf-8">
<title>Vora Kest Cleansers Trading L.L.C — Stationery</title>
<link href="https://fonts.googleapis.com/css2?family=Poppins:wght@300;400;500&family=Oswald:wght@500&family=Roboto:wght@400;500&display=swap" rel="stylesheet">
<style>
  :root{
    --stage:#dedede;
    --paper:#ffffff;
    --blue:#0a6ebd;
    --green:#6cbd2c;
    --ink:#3d3d3d;
    --muted:#777777;
    --rule:#8a8a8a;
    --red:#e0262b;
    --brand-green:#1d8a3a;
    --faint:#f1f5ee;
  }
  *{box-sizing:border-box;margin:0;padding:0}
  html,body{width:1200px;height:738px;overflow:hidden;background:var(--stage)}
  body{position:relative;font-family:"Poppins",sans-serif;color:var(--ink)}
  .sheet{position:absolute;background:var(--paper);box-shadow:0 1px 3px rgba(0,0,0,.18);overflow:hidden}

  .brand{position:absolute;display:flex;align-items:center;gap:5px}
  .brand-dot{border-radius:50%;border:3px solid var(--green);flex:none}
  .brand-name{font-family:"Poppins",sans-serif;font-weight:400;color:var(--blue);line-height:1;white-space:nowrap}
  .brand-sub{position:absolute;font-family:"Poppins",sans-serif;font-weight:300;color:var(--muted);letter-spacing:.5px;white-space:nowrap}

  .address{position:absolute;font-family:"Roboto",sans-serif;font-size:6.2px;line-height:7.7px;color:var(--ink);white-space:nowrap}
  .address .row{display:flex;align-items:center;gap:3px}
  .icon{width:5px;height:5px;fill:var(--blue);flex:none}

  .letterhead{left:66px;top:74px;width:452px;height:583px}
  .letterhead .divider{position:absolute;left:294px;top:42px;width:1px;height:54px;background:#999}
  .watermark{position:absolute;border-radius:50%;background:var(--faint);opacity:.7}
  .greeting{position:absolute;left:41px;top:168px;font-size:11.5px;font-weight:300}
  .letter-body{position:absolute;left:41px;top:203px;width:374px;font-size:6.4px;line-height:9.6px;font-weight:300;text-align:justify;color:#555}
  .letter-body p{margin-bottom:9.6px}
  .closing{position:absolute;left:41px;top:406px;font-size:6.4px;font-weight:300;color:#555}
  .signature{position:absolute;left:38px;top:430px;width:80px;height:36px;background:linear-gradient(90deg,rgba(10,110,189,.18),rgba(10,110,189,.06));border-radius:4px}

  .footer-rule{position:absolute;height:1px;background:var(--rule)}
  .partners{position:absolute;display:flex;gap:6px;align-items:center}
  .partner-badge{display:block;height:15px;border-radius:2px;flex:none}
  .partner-badge.fresh{width:46px;background:var(--brand-green)}
  .partner-badge.pro{width:46px;background:var(--red)}
  .partner-badge.khubrat{width:48px;height:12px;background:#9bb8d6}
  .membership-badge{position:absolute;width:104px;height:26px;border-radius:2px;background:var(--red)}

  .card-front{left:594px;top:114px;width:250px;height:143px;background:var(--blue)}
  .card-front svg.curve{position:absolute;left:0;top:0}
  .card-name{position:absolute;left:14px;top:26px;font-family:"Oswald",sans-serif;font-weight:500;color:#fff;font-size:7px;line-height:8.6px;text-transform:uppercase;white-space:nowrap}
  .card-name .title{font-size:5.6px}
  .card-front .address{color:#fff;left:14px;top:60px;font-size:5.2px;line-height:7.2px}
  .card-front .icon{fill:#fff}
  .card-back{left:866px;top:114px;width:250px;height:143px}
  .card-back .partners{left:0;right:0;top:57px;justify-content:center}
  .card-back .slogans{position:absolute;left:0;right:0;top:116px;text-align:center;font-family:"Roboto",sans-serif;font-size:6.4px;color:#555;letter-spacing:.2px;white-space:nowrap}

  .envelope-back{left:601px;top:312px;width:530px;height:230px}
  .envelope-front{left:547px;top:426px;width:530px;height:231px}
</style>
</head>
<body>

<svg width="0" height="0" style="position:absolute" aria-hidden="true">
  <symbol id="i-phone" viewBox="0 0 10 10"><path d="M2 0.5l2 0 1 2.5-1.3 1a6 6 0 0 0 2.3 2.3l1-1.3 2.5 1v2a1 1 0 0 1-1 1A8 8 0 0 1 1 1.5a1 1 0 0 1 1-1z"/></symbol>
  <symbol id="i-fax" viewBox="0 0 10 10"><rect x="2.5" y="0.5" width="5" height="3"/><rect x="0.5" y="4" width="9" height="4.5" rx="1"/></symbol>
  <symbol id="i-mobile" viewBox="0 0 10 10"><path d="M3 0h4a1 1 0 0 1 1 1v8a1 1 0 0 1-1 1H3a1 1 0 0 1-1-1V1a1 1 0 0 1 1-1zm0.5 1.2v6.6h3V1.2z"/></symbol>
  <symbol id="i-mail" viewBox="0 0 10 10"><path d="M0 2h10v6H0z"/></symbol>
  <symbol id="i-globe" viewBox="0 0 10 10"><circle cx="5" cy="5" r="4.6"/></symbol>
</svg>

<section class="sheet letterhead">
  <div class="watermark" style="left:130px;top:190px;width:192px;height:192px"></div>

  <div class="brand" style="left:41px;top:50px">
    <span class="brand-dot" style="width:34px;height:34px"></span>
    <span class="brand-name" style="font-size:24px">vora kest</span>
  </div>
  <div class="brand-sub" style="left:93px;top:81px;font-size:5.6px">CLEANSERS TRADING L.L.C</div>

  <div class="divider"></div>
  <div class="address" style="left:306px;top:43px">
    <div>Ras Kulaib - Next to Nuwar Plaza Mall</div>
    <div>Fanar Trade Tower - 614</div>
    <div>P.O.Box : 48207 Dubai - U.A.E</div>
    <div class="row" style="margin-top:2px"><svg class="icon"><use href="#i-phone"/></svg>00971 4 57 86 204</div>
    <div class="row"><svg class="icon"><use href="#i-fax"/></svg>00971 4 57 86 205</div>
    <div class="row"><svg class="icon"><use href="#i-mail"/></svg>info@vorakestclean.example</div>
    <div class="row"><svg class="icon"><use href="#i-globe"/></svg>www.vorakestclean.example</div>
  </div>

  <p class="greeting">Dear Mr. Harlow,</p>
  <div class="letter-body">
    <p>Lorem ipsum dolor sit amet, consectetur adipiscing elit. Donec orci purus, luctus vitae dignissim eu, iaculis sed purus. Vivamus faucibus, ipsum nec aliquet viverra, leo mauris condimentum ligula, sit amet sagittis enim ligula quis arcu. Nam egestas tortor id nisi porttitor mattis. In tortor ante, ultricies in suscipit a, tempus non massa. Vivamus et auctor mi. Fusce vel massa nulla. Phasellus nec eros mauris, et scelerisque orci.</p>
    <p>Donec malesuada orci vitae nulla accumsan porta a id massa. Quisque accumsan iaculis magna sit amet fringilla. Maecenas consequat, magna eget tincidunt semper, odio nibh rutrum mi, id feugiat ante nisi eu risus. Vestibulum nunc orci, rhoncus a placerat in, ultricies in mi. Cras mattis varius eros, vel fringilla nisi suscipit eget. Quisque scelerisque sagittis nulla at porttitor.</p>
    <p>Sed id augue vitae urna euismod commodo aliquet a quam. Pellentesque arcu velit, cursus et malesuada ut, consequat et diam. Nullam erat sem, rhoncus id ullamcorper vitae, rhoncus et arcu. In ultricies ultricies nulla, ut rutrum nisi iaculis at. Donec eu magna a metus ornare faucibus. Fusce aliquet faucibus ultricies. Morbi semper, est id tincidunt gravida, sem arcu adipiscing lacus, ac bibendum nulla leo eu purus. Quisque nec diam sed risus consectetur a cursus quis nibh. Vestibulum id purus lorem.</p>
    <p>It is a long established fact that a reader will be distracted by the readable content of a page when looking at its layout. The point of using Lorem Ipsum is that it has a more-or-less normal distribution of letters, as opposed to using 'Content here, content here', making it look like readable English. Many desktop publishing packages</p>
  </div>
  <p class="closing">Sincerely,</p>
  <div class="signature" role="img" aria-label="Handwritten signature of Evan Harlow"></div>

  <div class="footer-rule" style="left:41px;top:526px;width:374px"></div>
  <div class="partners" style="left:41px;top:544px">
    <span class="partner-badge fresh" role="img" aria-label="Pivo Fresh Range badge"></span>
    <span class="partner-badge pro" role="img" aria-label="Pivo Professional badge"></span>
    <span class="partner-badge khubrat" role="img" aria-label="Khubrat badge"></span>
  </div>
  <div class="membership-badge" role="img" aria-label="Saif Bin Harun membership badge" style="right:37px;top:538px"></div>
</section>

<section class="sheet card-front">
  <svg class="curve" width="250" height="143" viewBox="0 0 250 143" aria-hidden="true">
    <path d="M182 0 C100 20 100 123 184 143" fill="none" stroke="var(--green)" stroke-width="5"/>
    <path d="M186 0 C106 20 106 123 188 143 L250 143 L250 0 Z" fill="#fff"/>
  </svg>
  <div class="card-name">Sami Yousef Hamdan Jaber<br><span class="title">Director Manager</span><br><span class="title">+ 971 55 839 0 839</span></div>
  <div class="address">
    <div>Ras Kulaib - Next to Nuwar Plaza Mall</div>
    <div>Fanar Trade Tower - 614</div>
    <div>P.O.Box : 48207 Dubai - U.A.E</div>
    <div class="row" style="margin-top:3px"><svg class="icon"><use href="#i-phone"/></svg>00971 4 57 86 204</div>
    <div class="row"><svg class="icon"><use href="#i-mobile"/></svg>00971 4 57 86 205</div>
    <div class="row"><svg class="icon"><use href="#i-mail"/></svg>info@vorakestclean.example</div>
    <div class="row"><svg class="icon"><use href="#i-globe"/></svg>www.vorakestclean.example</div>
  </div>
  <div class="brand" style="left:142px;top:57px">
    <span class="brand-dot" style="width:26px;height:26px;border-width:2.5px"></span>
    <span class="brand-name" style="font-size:15px">vora kest</span>
  </div>
  <div class="brand-sub" style="left:173px;top:78px;font-size:4px">CLEANSERS TRADING L.L.C</div>
</section>

<section class="sheet card-back">
  <div class="partners">
    <span class="partner-badge fresh" role="img" aria-label="Pivo Fresh Range badge"></span>
    <span class="partner-badge pro" role="img" aria-label="Pivo Professional badge"></span>
    <span class="partner-badge khubrat" role="img" aria-label="Khubrat badge"></span>
  </div>
  <p class="slogans">PIVO FRESH RANGE &nbsp;-&nbsp; PIVO PROFESSIONAL &nbsp;-&nbsp; KHUBRAT</p>
</section>

<section class="sheet envelope-back">
  <svg width="530" height="80" viewBox="0 0 530 80" style="position:absolute;left:0;top:0" aria-hidden="true">
    <path d="M0 0 H530 L518 66 Q515 76 504 76 H26 Q15 76 13 66 Z" fill="var(--blue)"/>
    <circle cx="264" cy="40" r="14" fill="none" stroke="var(--green)" stroke-width="3"/>
  </svg>
</section>

<section class="sheet envelope-front">
  <div class="watermark" style="left:318px;top:40px;width:206px;height:206px"></div>
  <div class="brand" style="left:26px;top:30px">
    <span class="brand-dot" style="width:34px;height:34px"></span>
    <span class="brand-name" style="font-size:24px">vora kest</span>
  </div>
  <div class="brand-sub" style="left:78px;top:61px;font-size:5.6px">CLEANSERS TRADING L.L.C</div>
  <div class="address" style="left:78px;top:73px">
    <div>Ras Kulaib - Next to Nuwar Plaza Mall</div>
    <div>Fanar Trade Tower - 614</div>
    <div>P.O.Box : 48207 Dubai - U.A.E</div>
  </div>
  <div class="footer-rule" style="left:26px;top:173px;width:477px"></div>
  <div class="partners" style="left:26px;top:191px">
    <span class="partner-badge fresh" role="img" aria-label="Pivo Fresh Range badge"></span>
    <span class="partner-badge pro" role="img" aria-label="Pivo Professional badge"></span>
    <span class="partner-badge khubrat" role="img" aria-label="Khubrat badge"></span>
  </div>
  <div class="membership-badge" role="img" aria-label="Saif Bin Harun membership badge" style="right:27px;top:185px"></div>
</section>

</body>
</html>
```